Used Car Dealer seeks an Amazing Business Card Design

We are looking for a business card design that incorporates our logo and grabs the attention of anyone we give the business card to.

Looking to use the same colors as the logo. Our Logo choice is the black background with Red and Silver/Grey Lettering.

We also would like to see some embossed designs.

Target Market(s)

Used Car Buyers, Automotive, Auto

Industry/Entity Type

Automotive

Contact Information for Business Card

BVEL7K
Gordon Whitlock
482 Tarrow Lane
Suite 207
Brackton, OR 97412
Office (208) 555-0142
Cell (208) 555-0187
bvel7kga@quellmail.com
www.bvel7kga.com

Colors
ffffff
ee3036

Requirements
Must have
• Must include our logo (Black Background with Red and Silver/Grey Lettering)
Nice to have
• Embossed Design. Can be Single or Double Sided.

```html
<!DOCTYPE html>
<html lang="en">
<head>
<meta charset="utf-8">
<title>BVEL7K Business Card</title>
<link href="https://fonts.googleapis.com/css2?family=Roboto:wght@400;700&display=swap" rel="stylesheet">
<style>
  :root {
    --backdrop: #1c1c1c;
    --card: #262626;
    --emboss: #323232;
    --red: #ee3036;
    --silver: #c9c9c9;
    --white: #ffffff;
    --divider: #3a3a3a;
  }
  html, body {
    margin: 0;
    padding: 0;
    width: 1200px;
    height: 974px;
    overflow: hidden;
    background: var(--backdrop);
    font-family: "Roboto", Arial, sans-serif;
  }
  .canvas {
    position: relative;
    width: 1200px;
    height: 974px;
  }
  .card {
    position: absolute;
    top: 344px;
    width: 500px;
    height: 286px;
    background: var(--card);
    border-radius: 14px;
    box-shadow: 0 10px 30px rgba(0,0,0,0.45);
    overflow: hidden;
  }
  .card--front { left: 70px; }
  .card--back { left: 630px; }

  .brand-name {
    position: absolute;
    font-weight: 700;
    letter-spacing: 1px;
    line-height: 1;
  }
  .card--front .brand-name {
    left: 38px;
    top: 112px;
    font-size: 50px;
    color: var(--silver);
  }
  .card--back .brand-name {
    left: 0;
    right: 0;
    top: 110px;
    text-align: center;
    font-size: 66px;
    color: var(--emboss);
  }

  .divider {
    position: absolute;
    left: 262px;
    top: 56px;
    width: 1px;
    height: 120px;
    background: var(--divider);
  }

  .contact {
    position: absolute;
    left: 284px;
    top: 60px;
    color: var(--white);
    font-size: 13.5px;
    line-height: 1.45;
  }
  .contact__name {
    margin: 0 0 6px;
    font-size: 19px;
    font-weight: 700;
    color: var(--red);
    text-transform: uppercase;
  }
  .contact__list {
    list-style: none;
    margin: 0;
    padding: 0;
  }
  .contact__item {
    display: flex;
    align-items: center;
    gap: 7px;
  }
  .contact__item svg {
    width: 12px;
    height: 12px;
    flex: none;
  }
  .contact__address {
    margin: 8px 0 0 -18px;
    font-style: normal;
  }
</style>
</head>
<body>
<main class="canvas">

  <section class="card card--front" aria-label="Business card front">
    <div class="brand-name">BVEL7K</div>
    <div class="divider"></div>
    <div class="contact">
      <h1 class="contact__name">Gordon Whitlock</h1>
      <ul class="contact__list">
        <li class="contact__item">
          <svg viewBox="0 0 12 12" aria-hidden="true"><rect x="3" y="0.8" width="6" height="10.4" rx="1.2" fill="none" stroke="var(--red)" stroke-width="1.4"/><circle cx="6" cy="9.3" r="0.7" fill="var(--red)"/></svg>
          (208) 555-0187
        </li>
        <li class="contact__item">
          <svg viewBox="0 0 12 12" aria-hidden="true"><path d="M2.5 1 L4.6 1 L5.3 3.6 L4 4.6 Q5 7 7.4 8 L8.4 6.7 L11 7.4 L11 9.5 Q10.5 11 9 11 Q1 10 1 2.5 Q1 1 2.5 1 Z" fill="var(--red)"/></svg>
          (208) 555-0142
        </li>
        <li class="contact__item">
          <svg viewBox="0 0 12 12" aria-hidden="true"><rect x="0.7" y="2.2" width="10.6" height="7.6" rx="0.8" fill="var(--red)"/><path d="M1 2.6 L6 6.6 L11 2.6" fill="none" stroke="var(--card)" stroke-width="1"/></svg>
          bvel7kga@quellmail.com
        </li>
        <li class="contact__item">
          <svg viewBox="0 0 12 12" aria-hidden="true"><g fill="none" stroke="var(--red)" stroke-width="1.1"><circle cx="6" cy="6" r="5"/><ellipse cx="6" cy="6" rx="2.2" ry="5"/><path d="M1 6 H11 M2 3.3 H10 M2 8.7 H10"/></g></svg>
          www.bvel7kga.com
        </li>
      </ul>
      <address class="contact__address">
        482 Tarrow Lane, Suite 207<br>
        Brackton, OR 97412
      </address>
    </div>
  </section>

  <section class="card card--back" aria-label="Business card back">
    <div class="brand-name">BVEL7K</div>
  </section>

</main>
</body>
</html>
```